The Quiet Pantry Method: Reshape Your Habits Around Meals in Only 30 Days

I want a book cover for a paperback non-fiction book 30 day challenge to transform you relationship with your food, diet and lifestyle for longterm health and vitality. I would like to incorporate two photos on the front cover, one of a Greek salad and one of me the author. I have uploaded the four photos. Use which of each pair you think best. Because of my name, I want the photo on the cover. Otherwise folks assume Marla is a guy.
I am looking at best selling health books and they seem to be on the lighter side color-wise, with horizontal design. Green and orange seem to work most often, though my logo is a bluish turquoise (https://marlavoskin.com). I would imagine a light background, clear simple fonts. Looking forward to your designs!

Target Market(s)

Women around 35-40 confused by conflicting nutrition information but dedicated to better health haelthy

Industry/Entity Type

nutrition and wellness

Font styles to use
Serif

Colors
00AB8E
00BBA5
67D7C9
C6EFE9
E9F9F6
F0912C
F2A743
F7CA91
FBE8D2
FDF5EE
EE7325
F08F49
F5BC92
FAE3D3
FDF4ED

Requirements
Must have
• Clear simple look with room for an endorsement
Nice to have
• Hints of natural scenes and happy places
Should not have
• Dark or ominous feel

```html
<!DOCTYPE html>
<html lang="en">
<head>
<meta charset="utf-8">
<title>The Quiet Pantry Method – Cover Spread</title>
<link href="https://fonts.googleapis.com/css2?family=Oswald:wght@500;600&family=Montserrat:wght@400;500;600&display=swap" rel="stylesheet">
<style>
  :root {
    --teal: #1aa8b8;
    --green-rule: #00ab8e;
    --orange: #ee7325;
    --ink: #333333;
    --text: #555555;
    --logo-grey: #6f6f6f;
    --page: #ededed;
    --paper-light: #fbfbfb;
    --paper-shade: #d9d9d9;
    --white: #ffffff;
  }
  * { box-sizing: border-box; margin: 0; padding: 0; }
  html, body { width: 791px; height: 1200px; overflow: hidden; background: var(--page); }
  body { position: relative; font-family: "Montserrat", sans-serif; color: var(--text); }

  .spread {
    position: absolute; left: 26px; top: 350px; width: 739px; height: 500px;
    box-shadow: 0 6px 18px rgba(0,0,0,.18);
  }
  .panel { position: absolute; top: 0; height: 500px; overflow: hidden;
    background: radial-gradient(ellipse at 35% 30%, var(--paper-light) 0%, #ececec 55%, var(--paper-shade) 100%); }
  .back { left: 0; width: 347px; }
  .front { left: 398px; width: 341px; }

  .spine { position: absolute; left: 347px; top: 0; width: 51px; height: 500px; background: var(--teal); }
  .spine-title {
    position: absolute; left: 50%; top: 14px; transform-origin: 0 0;
    transform: translateX(12px) rotate(90deg);
    white-space: nowrap; font-family: "Montserrat", sans-serif; font-weight: 500;
    font-size: 19px; letter-spacing: .5px; color: var(--white);
  }

  /* title lockup */
  .kicker { position: absolute; font-family: "Montserrat", sans-serif; font-weight: 500;
    color: var(--orange); white-space: nowrap; transform-origin: 0 0; transform: rotate(-90deg); letter-spacing: 1px; }
  .title-top { position: absolute; font-family: "Oswald", sans-serif; font-weight: 600; color: var(--ink); line-height: 1; letter-spacing: -.5px; white-space: nowrap; }
  .title-main { position: absolute; font-family: "Oswald", sans-serif; font-weight: 600; color: var(--teal); line-height: 1; letter-spacing: -1px; white-space: nowrap; }

  .back .kicker { left: 14px; top: 104px; font-size: 11px; }
  .back .title-top { left: 30px; top: 24px; font-size: 29px; }
  .back .title-main { left: 29px; top: 52px; font-size: 48px; }
  .back-tagline { position: absolute; left: 190px; top: 34px; width: 150px; font-size: 11.5px; line-height: 16px;
    text-transform: uppercase; letter-spacing: .3px; color: #444; }

  .blurb { position: absolute; left: 16px; top: 128px; width: 303px; font-size: 6.8px; line-height: 8.8px; color: var(--text); }
  .author-photo-back { position: absolute; left: 16px; top: 239px; width: 119px; height: 181px;
    background: linear-gradient(180deg, #a9a9a9 0%, #8d8d8d 55%, #262626 56%, #1a1a1a 100%); }
  .bio { position: absolute; left: 145px; top: 238px; width: 182px; font-size: 6.8px; line-height: 8.6px; text-align: justify; color: var(--text); }

  .footer { position: absolute; left: 0; bottom: 0; width: 100%; height: 68px; background: var(--white);
    border-top: 5px solid var(--green-rule); display: flex; align-items: center; justify-content: center; gap: 8px; }
  .brand-dot { width: 22px; height: 22px; border-radius: 50%; background: var(--teal); }
  .brand-name { font-family: "Montserrat", sans-serif; font-weight: 400; font-size: 22px; color: var(--logo-grey); letter-spacing: -.3px; }

  .front .kicker { left: 14px; top: 176px; font-size: 17px; }
  .front .title-top { left: 40px; top: 32px; font-size: 44px; }
  .front .title-main { left: 39px; top: 84px; font-size: 68px; z-index: 2; }
  .salad-photo { position: absolute; right: 0; top: 0; width: 110px; height: 202px;
    border-bottom-left-radius: 100px 90px;
    background: radial-gradient(ellipse at 55% 55%, #c9b23a 0%, #8a9b3c 35%, #b0733a 70%, #d9d2c8 100%); }
  .front-band { position: absolute; left: 0; top: 202px; width: 100%; height: 45px; background: var(--orange);
    color: var(--white); font-family: "Montserrat", sans-serif; font-weight: 600; font-size: 12.5px;
    line-height: 16px; letter-spacing: .8px; text-align: center; text-transform: uppercase;
    display: flex; flex-direction: column; justify-content: center; }
  .author-photo-front { position: absolute; left: 97px; top: 262px; width: 159px; height: 170px;
    background: linear-gradient(180deg, #e4e4e4 0%, #d6d6d6 50%, #232323 51%, #161616 100%); }
</style>
</head>
<body>
  <main class="spread">
    <section class="panel back">
      <span class="kicker">THE QUIET</span>
      <span class="title-top">PANTRY</span>
      <span class="title-main">METHOD</span>
      <p class="back-tagline">Reshape<br>your habits<br>around meals<br>in only 30 days</p>

      <p class="blurb">Thirty days, one simple shift. This gentle guide helps you quiet the noise of conflicting nutrition advice and build calm, lasting habits around every meal. Each day brings a short reading, a small practice and a moment of reflection, so change feels natural rather than forced. By the end of the month you will know what nourishes you, why it matters and how to keep going with confidence, energy and ease for years to come.</p>

      <div class="author-photo-back" role="img" aria-label="Portrait photo of the author, Marla Voskin"></div>
      <p class="bio">Marla Voskin has spent decades helping families find their way back to simple, nourishing food. A counselor, author and speaker, she blends practical nutrition with warm, everyday wisdom drawn from her own kitchen table. Her approach is never about strict rules or guilt. Instead she invites readers to slow down, notice how food makes them feel and choose meals that bring real energy and joy. Over the years she has guided thousands of women through workshops, talks and one-to-one sessions, always with the same goal: lasting health that fits a real life. She lives near the coast, where she grows herbs, walks each morning and still believes the best meals begin with one honest ingredient and a little patience. This book gathers her most trusted methods into one clear, friendly month of practice.</p>

      <footer class="footer">
        <span class="brand-dot"></span>
        <span class="brand-name">MarlaVoskin</span>
      </footer>
    </section>

    <div class="spine">
      <span class="spine-title">THE QUIET PANTRY METHOD</span>
    </div>

    <section class="panel front">
      <div class="salad-photo" role="img" aria-label="Photo of a Greek salad in a wooden bowl with serving spoons"></div>
      <span class="kicker">THE QUIET</span>
      <span class="title-top">PANTRY</span>
      <span class="title-main">METHOD</span>
      <div class="front-band">
        <span>Reshape your habits around</span>
        <span>meals in only 30 days</span>
      </div>
      <div class="author-photo-front" role="img" aria-label="Portrait photo of the author, Marla Voskin"></div>
      <footer class="footer">
        <span class="brand-dot"></span>
        <span class="brand-name">MarlaVoskin</span>
      </footer>
    </section>
  </main>
</body>
</html>
```